New Business Card Design Project

We would like a business card that represents the sale of boat, home, auto, and life insurance.

The logo can change colors to meet the look of the design if needed.

Industry/Entity Type

Business

```html
<!DOCTYPE html>
<html lang="en">
<head>
<meta charset="utf-8">
<title>Halden Financial – Business Card</title>
<link href="https://fonts.googleapis.com/css2?family=Open+Sans:wght@400;600&display=swap" rel="stylesheet">
<style>
  :root {
    --backdrop: #3a302b;
    --card: #4a4a4a;
    --ink-light: #e6e6e6;
    --ink-muted: #cfcfcf;
    --accent: #3a8db3;
    --band-light: #e4e4e4;
    --divider: #8a8a8a;
  }
  * { margin: 0; padding: 0; box-sizing: border-box; }
  html, body {
    width: 1200px; height: 768px; overflow: hidden;
    background: var(--backdrop);
    font-family: "Open Sans", Arial, sans-serif;
  }
  .stage {
    position: relative; width: 1200px; height: 768px;
    display: flex; align-items: center; justify-content: center; gap: 40px;
  }
  .card {
    position: relative; width: 540px; height: 310px;
    background: var(--card);
    box-shadow: 0 10px 24px rgba(0,0,0,0.45);
    overflow: hidden;
  }
  .brand {
    position: absolute; display: flex; flex-direction: column; align-items: center;
  }
  .brand-row { display: flex; align-items: center; gap: 10px; }
  .brand-dot {
    width: 18px; height: 18px; border-radius: 50%; background: var(--accent);
  }
  .brand-name {
    color: var(--ink-light); font-weight: 600; font-size: 30px;
    letter-spacing: 4px; line-height: 1;
  }
  .brand-tagline {
    margin-top: 8px; color: var(--ink-muted); font-size: 16px; letter-spacing: 1px;
  }
  .card-front .brand { left: 0; right: 0; top: 118px; }
  .card-back .brand { left: 24px; width: 250px; top: 112px; }
  .card-back .brand-name { font-size: 22px; letter-spacing: 3px; }
  .card-back .brand-dot { width: 14px; height: 14px; }
  .card-back .brand-tagline { font-size: 13px; }
  .divider {
    position: absolute; left: 300px; top: 40px; width: 1px; height: 210px;
    background: var(--divider);
  }
  .contact {
    position: absolute; left: 326px; top: 44px; width: 200px; color: var(--ink-light);
  }
  .contact-name { font-size: 17px; font-weight: 600; }
  .contact-title { font-size: 13px; color: var(--ink-muted); margin-bottom: 16px; }
  .contact-line {
    display: flex; align-items: center; gap: 8px; font-size: 11.5px; line-height: 18px;
  }
  .contact-line svg { width: 11px; height: 11px; fill: var(--ink-light); flex: none; }
  .contact-address { margin-top: 8px; font-size: 11.5px; line-height: 16px; }
  .bands { position: absolute; left: 0; bottom: 0; width: 540px; height: 22px; }
</style>
</head>
<body>
<main class="stage">
  <section class="card card-front">
    <div class="brand">
      <div class="brand-row">
        <span class="brand-dot"></span>
        <span class="brand-name">HALDEN FINANCIAL</span>
      </div>
      <span class="brand-tagline">investments &amp; insurance</span>
    </div>
  </section>

  <section class="card card-back">
    <div class="brand">
      <div class="brand-row">
        <span class="brand-dot"></span>
        <span class="brand-name">HALDEN FINANCIAL</span>
      </div>
      <span class="brand-tagline">investments &amp; insurance</span>
    </div>

    <div class="divider"></div>

    <div class="contact">
      <p class="contact-name">Your Long Name</p>
      <p class="contact-title">Your Title</p>
      <p class="contact-line">
        <svg viewBox="0 0 12 12"><path d="M2 1h2l1 3-1.5 1a6 6 0 0 0 3.5 3.5L8 7l3 1v2a1 1 0 0 1-1 1A9 9 0 0 1 1 2a1 1 0 0 1 1-1z"/></svg>
        000 0 0 000 00
      </p>
      <p class="contact-line">
        <svg viewBox="0 0 12 12"><rect x="3" y="0.5" width="6" height="11" rx="1"/><rect x="4" y="2" width="4" height="6" fill="#4a4a4a"/></svg>
        (00) 0 0 0000 0000
      </p>
      <p class="contact-line">
        <svg viewBox="0 0 12 12"><rect x="0.5" y="2" width="11" height="8"/><path d="M1 2.5l5 4 5-4" stroke="#4a4a4a" fill="none"/></svg>
        yourname@yourwebsite.com
      </p>
      <p class="contact-line">
        <svg viewBox="0 0 12 12"><circle cx="6" cy="6" r="5.5"/><path d="M0.5 6h11M6 0.5c-3 3-3 8 0 11M6 0.5c3 3 3 8 0 11" stroke="#4a4a4a" fill="none" stroke-width="0.8"/></svg>
        www.yourwebsite.com
      </p>
      <p class="contact-address">Your office or residential address in just two line with pin code.</p>
    </div>

    <svg class="bands" viewBox="0 0 540 22" aria-hidden="true">
      <polygon points="0,10 250,10 262,22 0,22" fill="var(--accent)"/>
      <polygon points="250,10 540,4 540,22 262,22" fill="var(--band-light)"/>
    </svg>
  </section>
</main>
</body>
</html>
```